Business Card Design Project

We need a hip business card! We are a bakery that specializes in bite sized treats! We do not like foo-foo things, rather have a hip, edgy nature about our style. Our head baker has lots of tattoos....basically, we are not going for the tea party look. We have uploaded our logo, which has a character in it...because we still want to be fun and friendly to little peeps...

Colors: Red and Black
Use : Existing logo
Info: name, address, telephone #, email, URL

Industry/Entity Type

Bakery

Requirements
Must have
• logo: will upload
font: serfiffic grunge
feel: hip and cool, somewhat edgy yet still fun

```html
<!DOCTYPE html>
<html lang="en">
<head>
<meta charset="utf-8">
<title>Nibble Den Bakery – Business Card</title>
<link rel="stylesheet" href="https://fonts.googleapis.com/css2?family=Rye&family=Croissant+One&display=swap">
<style>
  :root {
    --backdrop: #1f2124;
    --card: #ffffff;
    --ink: #111111;
    --devil-red: #e8110f;
    --text-red: #e0161b;
    --icon-grey: #6d7f98;
  }
  * { margin: 0; padding: 0; box-sizing: border-box; }
  html, body {
    width: 1200px; height: 900px; overflow: hidden;
    background: var(--backdrop);
  }
  .stage { position: relative; width: 1200px; height: 900px; }

  .card {
    position: absolute;
    background: var(--card);
    overflow: hidden;
  }
  .card--front { left: 92px; top: 101px; width: 510px; height: 283px; }
  .card--back  { left: 568px; top: 455px; width: 512px; height: 284px; }

  /* front */
  .mascot {
    position: absolute;
    border-radius: 48% 48% 50% 50% / 40% 40% 60% 60%;
    background: radial-gradient(circle at 45% 40%, #f23a2c 0%, var(--devil-red) 60%, #c70c0a 100%);
  }
  .card--front .mascot { left: 44px; top: 86px; width: 140px; height: 100px; }
  .brand {
    position: absolute; left: 218px; top: 106px;
    width: 262px;
    font-family: "Rye", serif;
    line-height: 1;
    white-space: nowrap;
  }
  .brand__name {
    display: block;
    font-size: 35px;
    color: var(--ink);
  }
  .brand__sub {
    display: block;
    margin-top: 8px;
    font-size: 18px;
    text-align: right;
    color: var(--text-red);
  }

  /* back */
  .person {
    position: absolute; left: 54px; top: 46px;
    font-family: "Croissant One", serif;
    font-size: 20px; font-weight: 400; letter-spacing: 0.5px;
    color: var(--text-red);
  }
  .contact-list {
    position: absolute; left: 64px; top: 106px;
    list-style: none;
    font-family: "Croissant One", serif;
    font-size: 12.5px;
    color: var(--text-red);
  }
  .contact-list li {
    display: flex; align-items: center; gap: 6px;
    height: 19px;
    white-space: nowrap;
  }
  .contact-icon {
    width: 16px; height: 16px; flex: none;
    border-radius: 3px; background: var(--icon-grey);
  }
  .contact-icon--phone { border-radius: 50%; background: var(--devil-red); }
  .web-links {
    position: absolute; right: 122px; top: 232px;
    font-family: "Croissant One", serif;
    font-size: 12.5px; line-height: 21px;
    color: var(--text-red);
    text-align: right;
    white-space: nowrap;
  }
  .card--back .mascot {
    left: 360px; top: 12px; width: 210px; height: 190px;
  }
</style>
</head>
<body>
<main class="stage">

  <section class="card card--front" aria-label="Business card front">
    <div class="mascot" role="img" aria-label="Red devil bakery mascot holding a cupcake and a pitchfork"></div>
    <div class="brand">
      <span class="brand__name">NIBBLE DEN</span>
      <span class="brand__sub">bakery</span>
    </div>
  </section>

  <section class="card card--back" aria-label="Business card back">
    <h1 class="person">MARCO REYES</h1>
    <ul class="contact-list">
      <li><span class="contact-icon contact-icon--phone"></span>: 555.204.7731</li>
      <li><span class="contact-icon"></span>: Nibble Den Bakery</li>
      <li><span class="contact-icon"></span>: @NIBBLEDENBAKERY</li>
      <li><span class="contact-icon"></span>: NIBBLEDENBAKERY</li>
    </ul>
    <div class="web-links">
      <div>HELLO@NIBBLEDENBAKERY.COM</div>
      <div>WWW.NIBBLEDENBAKERY.COM</div>
    </div>
    <div class="mascot" role="img" aria-label="Large red devil bakery mascot holding a cupcake, cropped at the card edge"></div>
  </section>

</main>
</body>
</html>
```